Zielgruppe
Wir betreiben eine Bäckerei mit Kaffeehaus als Nahversorger in A-3032 Lindenbach. Das design soll natürlich unsere Kunden ansprechen.
Aufgabenstellung
Es wird ein neuer Schriftzug horizontal für das Sanierungsobjekt gesucht. Folgende Vorgaben sind wünschenswert:
Schriftzug - Außenbeschilderung;
Schriftzug -Cafe- linksbündig, Schriftzug -Kleffinger- mittig, Schriftzug -Bäckerei- rechstbündig. Die Außenbeschilderung soll ca. 5m lang und ca. 70cm hoch sein. Siehe auch Bestandsobjekt im Anhang. Vorraussetzung ist, das das Design auf ALU oder Plexiglas folierbar ist.
Familienwappen;
Eine Druckversion ist im Anhang ersichtlich, eine vereinfachte Darstellung wäre durchaus möglich durch etwa Konturen/ Linien etc..
Farben;
Am Foto ersichtlich die neue Farbe der Fassade links und rechts.
Banner für zwischen den Fenstern - vertikal;
1x Design für Bäckerei (Semmel/ Brötchen, Korb mit Gebäck, etc.), Schriftzug oben -Bäckerei-, Schriftzug unten -Kleffinger-.
1x Design für Cafe (Kaffeetasse, Cupcake, etc), Schriftzug oben -Cafe-, Schriftzug unten -Kleffinger-.
Designvorschlag; helle Schrift auf dunklem Hintergrund- weinrot, smaragtgrün, dunkelblau???
Natürlich sind auch alternative/ abweichende Vorschläge wünschenswert.
Wir freuen uns auf die Designs !!!

```html
<!DOCTYPE html>
<html lang="de">
<head>
<meta charset="utf-8">
<title>Kleffinger – Außenbeschilderung</title>
<link href="https://fonts.googleapis.com/css2?family=Yellowtail&family=Marcellus&family=Open+Sans:wght@400;600&display=swap" rel="stylesheet">
<style>
  :root {
    --wine: #be1e2d;
    --white: #ffffff;
    --bg: #ffffff;
    --art: #d9505c;
  }
  * { margin: 0; padding: 0; box-sizing: border-box; }
  html, body { width: 1200px; height: 1200px; overflow: hidden; background: var(--bg); }
  .canvas { position: relative; width: 1200px; height: 1200px; }

  .fascia {
    position: absolute; left: 115px; top: 328px; width: 983px; height: 89px;
    background: var(--wine);
  }
  .fascia::before {
    content: ""; position: absolute; inset: 6px;
    border: 3px solid var(--white);
  }
  .script {
    font-family: "Yellowtail", cursive;
    color: var(--white);
    text-shadow: 2px 3px 3px rgba(0,0,0,.45);
    position: absolute; line-height: 1; white-space: nowrap;
  }
  .fascia .script { font-size: 56px; top: 14px; }
  .fascia .cafe { left: 94px; }
  .fascia .baeckerei { left: 710px; }
  .brand {
    font-family: "Marcellus", serif;
    color: var(--white);
    position: absolute; line-height: 1; white-space: nowrap;
  }
  .fascia .brand { left: 270px; width: 375px; top: 22px; font-size: 48px; text-align: center; letter-spacing: 1px; }

  .panel {
    position: absolute; top: 448px; width: 258px; height: 561px;
    background: var(--wine);
  }
  .panel::before {
    content: ""; position: absolute; left: 14px; top: 14px; right: 14px; bottom: 14px;
    border: 2px solid var(--white);
  }
  .panel::after {
    content: ""; position: absolute; left: 10px; right: 10px; bottom: 9px;
    height: 1px; background: rgba(255,255,255,.35);
  }
  .panel-bakery { left: 330px; }
  .panel-cafe { left: 617px; }
  .panel .script { left: 0; width: 100%; text-align: center; }
  .panel-bakery .script { top: 32px; font-size: 50px; }
  .panel-cafe .script { top: 26px; font-size: 64px; }
  .illustration { position: absolute; background: var(--art); border-radius: 8px; }
  .panel-bakery .illustration { left: 23px; top: 183px; width: 213px; height: 105px; }
  .panel-cafe .illustration { left: 55px; top: 146px; width: 147px; height: 150px; }
  .panel .brand { left: 0; width: 100%; text-align: center; top: 349px; font-size: 21px; }
  .tagline {
    position: absolute; left: 0; width: 100%; top: 372px; text-align: center;
    font-family: "Open Sans", sans-serif; font-size: 10.5px; line-height: 13.5px;
    color: var(--white); letter-spacing: .3px; padding-right: 8px;
  }
  .crest { position: absolute; left: 86px; top: 408px; width: 84px; height: 97px; background: var(--art); border-radius: 6px 6px 40px 40px; }
  .crest-caption {
    position: absolute; left: 0; width: 100%; top: 512px; text-align: center;
    font-family: "Open Sans", sans-serif; font-size: 7px; color: var(--white); padding-right: 8px;
  }
</style>
</head>
<body>
<div class="canvas">
  <div class="fascia">
    <span class="script cafe">Cafe</span>
    <span class="brand">KLEFFINGER</span>
    <span class="script baeckerei">Bäckerei</span>
  </div>

  <div class="panel panel-bakery">
    <span class="script">Bäckerei</span>
    <div class="illustration" role="img" aria-label="Illustration: Brotlaib im Kreis mit Ährenkranz"></div>
    <span class="brand">KLEFFINGER</span>
    <p class="tagline">DIE BÄCKEREI IN<br>LINDENBACH</p>
    <div class="crest" role="img" aria-label="Familienwappen"></div>
    <p class="crest-caption">FAMILIENWAPPEN SEIT 1412</p>
  </div>

  <div class="panel panel-cafe">
    <span class="script">Cafe</span>
    <div class="illustration" role="img" aria-label="Illustration: dampfende Kaffeetasse mit Kaffeebohnen"></div>
    <span class="brand">KLEFFINGER</span>
    <p class="tagline">DIE BÄCKEREI IN<br>LINDENBACH</p>
    <div class="crest" role="img" aria-label="Familienwappen"></div>
    <p class="crest-caption">FAMILIENWAPPEN SEIT 1412</p>
  </div>
</div>
</body>
</html>
```